Design the Keystone HR business card for my new business

I've just had a logo designed (attached) for my new business doing HR consulting. I'm a one person operation at this stage, my aim is to provide support and help to small to medium sized businesses with their people objectives or issues.

I'm not really into anything overly flashy, I'm not a PR or marketing agency. I'd like my card to look modern, professional and not gimmicky.

I'm thinking black front (to go with logo), double sided with details on the back, maybe in a different colour?

Logo attached in several different formats.

Front of the card to have logo and added text: People and Development Solutions

Back of the card to also feature logo in some way and say:
Megan Tulloch
PO Box (TBA)
Marrowvale QLD 4391
0438 512 976
megan@keystonehr.com.au
www.keystonehr.com.au

Target Market(s)

Small to medium businesses / business owners.

Industry/Entity Type

Marketing

Requirements
Must have
• Double sided business card.
Should not have
• Anything overly gimmicky.

```html
<!DOCTYPE html>
<html lang="en">
<head>
<meta charset="utf-8">
<title>Keystone HR Consulting – Business Card</title>
<link href="https://fonts.googleapis.com/css2?family=Inter:wght@300;400;700&display=swap" rel="stylesheet">
<style>
  :root {
    --stage-light: #ffffff;
    --stage-edge: #ececec;
    --card-black: #000000;
    --text-white: #ffffff;
    --text-muted: #b5b5b5;
    --violet: #9b3fd6;
    --violet-deep: #5a1c86;
  }
  * { margin: 0; padding: 0; box-sizing: border-box; }
  html, body { width: 1200px; height: 900px; overflow: hidden; }
  body {
    background: radial-gradient(ellipse at center, var(--stage-light) 30%, var(--stage-edge) 100%);
    font-family: "Inter", Arial, sans-serif;
    position: relative;
  }
  .card {
    position: absolute;
    top: 127px;
    width: 395px;
    height: 653px;
    background: var(--card-black);
    border-radius: 40px;
    overflow: hidden;
  }
  .card--front { left: 147px; }
  .card--back { left: 647px; }

  .brand {
    position: absolute;
    left: 28px;
    top: 249px;
    height: 125px;
    display: flex;
    align-items: center;
    gap: 28px;
  }
  .brand__mark {
    width: 125px;
    height: 125px;
    border-radius: 50%;
    background: var(--violet);
    flex: none;
  }
  .brand__name {
    color: var(--text-white);
    font-weight: 300;
    line-height: 1;
    white-space: nowrap;
  }
  .brand__title { font-size: 46px; letter-spacing: -1px; display: block; }
  .brand__sub { font-size: 23px; display: block; margin-top: 8px; }

  .tagline {
    position: absolute;
    left: 0;
    right: 0;
    top: 403px;
    text-align: center;
    color: var(--text-muted);
    font-size: 15px;
    font-weight: 300;
    letter-spacing: 0.8px;
  }

  .contact {
    position: absolute;
    left: 31px;
    top: 52px;
    color: var(--text-white);
    font-size: 19px;
    line-height: 26px;
  }
  .contact__name { font-weight: 700; font-size: 22px; margin-bottom: 31px; }
  .contact__address { margin-bottom: 25px; }
  .contact__row { display: flex; }
  .contact__label { font-weight: 700; width: 39px; }

  .back-accent {
    position: absolute;
    left: 100px;
    top: 310px;
    width: 460px;
    height: 460px;
    border-radius: 50%;
    background: radial-gradient(circle at 45% 55%, var(--violet) 0%, var(--violet-deep) 45%, var(--card-black) 72%);
  }
</style>
</head>
<body>
  <section class="card card--front">
    <div class="brand">
      <div class="brand__mark"></div>
      <div class="brand__name">
        <span class="brand__title">Keystone</span>
        <span class="brand__sub">HR Consulting</span>
      </div>
    </div>
    <p class="tagline">People and Development Solutions</p>
  </section>

  <section class="card card--back">
    <div class="back-accent" role="img" aria-label="Large violet brand decoration"></div>
    <div class="contact">
      <p class="contact__name">Megan Tulloch</p>
      <p class="contact__address">PO Box (TBA)<br>Marrowvale QLD 4391</p>
      <p class="contact__row"><span class="contact__label">T.</span><span>0438 512 976</span></p>
      <p class="contact__row"><span class="contact__label">E.</span><span>megan@keystonehr.com.au</span></p>
      <p class="contact__row"><span class="contact__label">W.</span><span>www.keystonehr.com.au</span></p>
    </div>
  </section>
</body>
</html>
```